Flyer Design Project

We need a flyer design for a 1 year old domestic cleaning company based in Wiltshire, England. We provide households with high quality, hard working cleaners. We would like to see designs which use blue (the colour on the logo attatched). The final design should communicate a clean, premier and thorough service in a clear and bold way. We would like the flyer to be A5 with a single sided design. We have attached an A5 word document with the words we would like to be used in the design, what we need is for you to give it some life, colour, artwork and a professional touch. We are perfectionsists which we would like to illustrate to our customer through this flyer.
Updates

payment has been guaranteed!

Sorry..... please no pictures of females on the designs. many thanks

Target Market(s)

females with higher than average income, aged 30-50. Have families and work 9-5.

Industry/Entity Type

It Company

Requirements
Must have
• The flyer must include the logo attatched and the words in the A5 document attatched. With RELIABLE CLEANERS preferably the headline. A5 - single sided.
The Flyer must also include our introductory offer.....
First Clean FREE
Allow us to demonstrate our standards

this should be emphasised.

PLEASE NOTE: can this be added to the list of words on the flyer please:

Ironing service - one day turn around
Nice to have
• some pictures - nothing cheesey. Again, pictures should communicate our modern professional approach.

```html
<!DOCTYPE html>
<html lang="en">
<head>
<meta charset="utf-8">
<title>Hartwell Cleaners – Reliable Cleaners Flyer</title>
<link rel="stylesheet" href="https://fonts.googleapis.com/css2?family=Arvo:wght@400;700&family=Arimo:wght@400;700&display=swap">
<style>
  :root {
    --page: #ffffff;
    --blue-deep: #0f34b8;
    --blue-main: #1545cf;
    --blue-light: #2f6ee6;
    --blue-pale: #4a8cf0;
    --orange: #f5a01a;
    --white: #ffffff;
    --photo-warm: #8a4a2a;
    --photo-light: #e9e6e2;
  }
  * { box-sizing: border-box; margin: 0; padding: 0; }
  html, body { width: 870px; height: 1200px; overflow: hidden; background: var(--page); }
  .flyer {
    position: absolute; left: 28px; top: 28px;
    width: 808px; height: 1144px; overflow: hidden;
    background: var(--blue-main);
    font-family: "Arvo", "Rockwell", serif; color: var(--white);
  }
  .hero-photo {
    position: absolute; left: 0; top: 0; width: 808px; height: 600px;
    background: linear-gradient(180deg, var(--photo-light) 0%, #d9d3cd 36%, #b0704a 52%, var(--photo-warm) 72%, #5e2c16 100%);
  }
  .swoosh { position: absolute; left: 0; top: 0; width: 808px; height: 1144px; }
  .brand-badge {
    position: absolute; left: 504px; top: 612px; width: 240px; height: 240px;
    border-radius: 50%; background: var(--white);
    border: 9px solid var(--blue-light);
    display: flex; flex-direction: column; align-items: center; justify-content: center;
    color: var(--blue-deep); text-align: center;
    font-family: "Arimo", Arial, sans-serif;
  }
  .brand-name { font-size: 23px; font-weight: 700; line-height: 1.1; white-space: nowrap; }
  .brand-tagline { font-size: 14px; font-weight: 700; margin-top: 3px; white-space: nowrap; }
  .headline {
    position: absolute; left: 56px; top: 664px;
    font-size: 68px; font-weight: 400; line-height: 1.0;
  }
  .offer {
    position: absolute; left: 48px; top: 828px;
    border-left: 7px solid var(--orange); padding-left: 12px;
  }
  .offer-title { font-size: 38px; line-height: 1.05; }
  .offer-title .free { color: var(--orange); }
  .offer-sub { font-size: 19px; margin-top: 4px; line-height: 1.2; }
  .services {
    position: absolute; left: 68px; top: 912px;
    font-size: 16px; line-height: 28px; list-style: none; white-space: nowrap;
  }
  .divider { position: absolute; left: 68px; top: 1008px; width: 428px; height: 2px; background: var(--white); }
  .contact-phone { position: absolute; left: 68px; top: 1018px; font-size: 33px; line-height: 1.2; white-space: nowrap; }
  .contact-email { position: absolute; left: 68px; top: 1072px; font-size: 17px; line-height: 1.2; white-space: nowrap; }
</style>
</head>
<body>
  <main class="flyer">
    <div class="hero-photo" role="img" aria-label="Photo: person vacuuming a polished wooden floor in a bright modern living room"></div>

    <svg class="swoosh" viewBox="0 0 808 1144" aria-hidden="true">
      <path d="M0 572 Q 340 420 808 380 L808 1144 L0 1144 Z" fill="var(--blue-light)"/>
      <path d="M0 606 Q 360 460 808 430 L808 1144 L0 1144 Z" fill="var(--blue-main)"/>
      <circle cx="624" cy="732" r="168" fill="none" stroke="var(--blue-light)" stroke-width="24" opacity="0.55"/>
      <circle cx="624" cy="732" r="220" fill="none" stroke="var(--blue-pale)" stroke-width="14" opacity="0.3"/>
    </svg>

    <div class="brand-badge">
      <span class="brand-name">Hartwell Cleaners</span>
      <span class="brand-tagline">Premier Domestic Cleaners</span>
    </div>

    <h1 class="headline">RELIABLE<br>CLEANERS!</h1>

    <section class="offer">
      <p class="offer-title">First Clean <span class="free">FREE</span></p>
      <p class="offer-sub">Allow us to demonstrate our standards</p>
    </section>

    <ul class="services">
      <li>Personalised service • Constantly thorough</li>
      <li>Hassel free • Insured • Regular weekly cleans • No contracts</li>
      <li>Ironing service - one day turn around</li>
    </ul>

    <div class="divider"></div>
    <p class="contact-phone">Tele: 07700900417</p>
    <p class="contact-email">Email: hartwellcleaners@mailbox.co.uk</p>
  </main>
</body>
</html>
```